Redgum Wrecking P/L business card

I already have a EPS logo design that I wish to use however, the company is a demolition company based on the Central Coast of NSW Australia. The company is called "Redgum Wrecking P/L".

We offer demolition services such as Residential, Commercial, Civil, Asbestos removal, Excavation and Tree removal that are required to be displayed on the rear of the business card.

We currently have 4 personnel that require business cards with their specific contact details.

The logo is mid blue on a white background and the remainder is black text on a whiter card.

The eps logo supplied should only be displayed as a logo without the text.

Target Market(s)

People, governments, companies requiring demolition services on the east coast of NSW, specifically Central Coast, Sydney and Newcastle locations.

Industry/Entity Type

Business

Contact Information for Business Card

There are four cards required
First card:
Martin Ellory
Operations Director
Mobile No. 0451 872164
E: info@redgumwreck.example.com.au
www.redgumwreck.example.com.au
Second card:
Peter Hollis
Project Director
Company Mobile: 0451 872164
Personal Mobile: 0426 158 309
www.redgumwreck.example.com.au
Third card:
Simon Brady
Project Director
Company Mobile: 0451 872 164
Personal Mobile: 0433 917 482
www.redgumwreck.example.com.au
Fourth card:
Lewis Thornby
General Manager
Personal Mobile: 0447 261 835
www.redgumwreck.example.com.au

Font styles to use
Other font styles liked:
• Helvetica

Colors
33a6d7

Requirements
Must have
• The RW logo (without the text of Redgum Wrecking)
Horizontal layout with logo on top left hand corner
Services provision on the rear of the card
Nice to have
• Logo on top left corner
Text should be something like Helvetica
Should not have
• Do not include the text that is incorporated in the EPS file I sent ….just the logo

```html
<!DOCTYPE html>
<html lang="en">
<head>
<meta charset="utf-8">
<title>Redgum Wrecking P/L – Business Card</title>
<link rel="stylesheet" href="https://fonts.googleapis.com/css2?family=Arimo:wght@400;500&display=swap">
<style>
  :root {
    --brand-teal: #21a2b8;
    --card-white: #f4f4f4;
    --ink-grey: #5a5a5a;
    --ink-light: #ffffff;
    --page-bg: #e6e6e4;
    --card-shadow: rgba(0, 0, 0, 0.18);
  }
  * { margin: 0; padding: 0; box-sizing: border-box; }
  html, body {
    width: 1200px;
    height: 900px;
    overflow: hidden;
    background: var(--page-bg);
    font-family: "Arimo", Helvetica, Arial, sans-serif;
  }
  .sheet {
    width: 1200px;
    height: 900px;
    display: flex;
    flex-direction: column;
    align-items: center;
    justify-content: center;
    gap: 56px;
  }
  .card {
    position: relative;
    width: 600px;
    height: 343px;
    box-shadow: 0 6px 18px var(--card-shadow);
  }
  .card--back { background: var(--brand-teal); color: var(--ink-light); }
  .card--front { background: var(--card-white); color: var(--ink-grey); }

  .wordmark {
    font-weight: 400;
    letter-spacing: -2px;
    line-height: 1;
  }
  .card--back .wordmark {
    position: absolute;
    left: 268px;
    top: 72px;
    font-size: 64px;
    color: var(--ink-light);
  }
  .card--front .wordmark {
    position: absolute;
    left: 48px;
    top: 42px;
    font-size: 58px;
    color: var(--brand-teal);
  }

  .services {
    position: absolute;
    left: 150px;
    top: 172px;
    font-size: 15px;
    line-height: 22px;
    letter-spacing: 0.4px;
  }

  .contact {
    position: absolute;
    left: 318px;
    top: 178px;
  }
  .contact__name {
    font-size: 21px;
    font-weight: 400;
    color: var(--ink-grey);
  }
  .contact__role {
    margin-top: 4px;
    font-size: 13px;
    color: var(--brand-teal);
  }
  .contact__list {
    list-style: none;
    margin-top: 16px;
    font-size: 14px;
    line-height: 23px;
  }
  .contact__item {
    display: flex;
    align-items: center;
    gap: 10px;
  }
  .contact__icon {
    width: 12px;
    height: 12px;
    flex: none;
  }
</style>
</head>
<body>
<main class="sheet">
  <section class="card card--back" aria-label="Card back">
    <div class="wordmark">RW</div>
    <p class="services">
      Residential | Commercial | Civil | Asbestos removal<br>
      Excavation and Tree removal
    </p>
  </section>

  <section class="card card--front" aria-label="Card front">
    <div class="wordmark">RW</div>
    <div class="contact">
      <h1 class="contact__name">Martin Ellory</h1>
      <p class="contact__role">Operations Director</p>
      <ul class="contact__list">
        <li class="contact__item">
          <svg class="contact__icon" viewBox="0 0 12 12" aria-hidden="true">
            <rect x="3" y="0.5" width="6" height="11" rx="1" fill="none" stroke="var(--brand-teal)" stroke-width="1.2"/>
            <circle cx="6" cy="9.4" r="0.7" fill="var(--brand-teal)"/>
          </svg>
          <span>0451 872164</span>
        </li>
        <li class="contact__item">
          <svg class="contact__icon" viewBox="0 0 12 12" aria-hidden="true">
            <rect x="0.6" y="2" width="10.8" height="8" fill="none" stroke="var(--brand-teal)" stroke-width="1.2"/>
            <path d="M0.8 2.3 L6 6.5 L11.2 2.3" fill="none" stroke="var(--brand-teal)" stroke-width="1.2"/>
          </svg>
          <span>info@redgumwreck.example.com.au</span>
        </li>
        <li class="contact__item">
          <svg class="contact__icon" viewBox="0 0 12 12" aria-hidden="true">
            <circle cx="6" cy="6" r="5.4" fill="var(--brand-teal)"/>
            <path d="M1 6 H11 M6 0.8 C3.5 3.5 3.5 8.5 6 11.2 M6 0.8 C8.5 3.5 8.5 8.5 6 11.2" fill="none" stroke="var(--card-white)" stroke-width="0.9"/>
          </svg>
          <span>www.redgumwreck.example.com.au</span>
        </li>
      </ul>
    </div>
  </section>
</main>
</body>
</html>
```